Amber Ridge Publishing Web Page Design

Design a website for my new start up publishing company - Amber Ridge Publishing, the first work published by ARP with be a new book by M.R. Theodor called Silent Ledger. The prototype for the book cover is attached.

Target Market(s)

Worldwide, all readers of mystery, fiction, etc.

Industry/Entity Type

Book Publisher

Coding

Coded - Design and coding required

Number of Pages Required

1 page

```html
<!DOCTYPE html>
<html lang="en">
<head>
<meta charset="utf-8">
<title>Amber Ridge Publishing</title>
<link href="https://fonts.googleapis.com/css2?family=Montserrat:wght@300;400;500;600;700;800;900&family=Courgette&display=swap" rel="stylesheet">
<style>
:root{
  --teal:#1cb3c6;
  --teal-deep:#16a6b9;
  --yellow:#e5c636;
  --red:#a8190b;
  --ink:#151515;
  --text:#3a3a3a;
  --muted:#6e6e6e;
  --navy:#0f1120;
  --white:#ffffff;
}
*{margin:0;padding:0;box-sizing:border-box}
html,body{width:1200px;height:4227px;overflow:hidden;background:var(--white)}
body{position:relative;font-family:"Montserrat",sans-serif;color:var(--text)}
.abs{position:absolute}
.btn{position:absolute;display:flex;align-items:center;justify-content:center;background:var(--yellow);color:var(--white);font-weight:700;font-size:15px;border-radius:20px;text-decoration:none}
.display{font-family:"Montserrat",sans-serif;font-weight:900;color:var(--ink);letter-spacing:-0.5px}
.body-copy{font-size:13.5px;line-height:26.5px;color:var(--muted);font-weight:400}

/* header */
.hero-shape{position:absolute;left:0;top:0}
.logo{left:89px;top:22px;font-size:54px;font-weight:900;color:var(--ink);letter-spacing:1px}
.nav{position:absolute;top:41px;display:flex;gap:0}
.nav a{position:absolute;font-size:14px;font-weight:500;color:var(--ink);text-decoration:none;white-space:nowrap}
.hero-title{left:89px;top:306px;font-size:48px;line-height:55px}
.hero-text{left:89px;top:478px;width:350px;font-size:13.5px;line-height:24.5px;color:var(--muted)}
.cover{position:absolute;border-radius:3px;box-shadow:18px 22px 30px rgba(0,0,0,.35)}
.cover-main{background:linear-gradient(160deg,#101a4a 0%,#2a3b8c 45%,#5d6fbf 60%,#1c2560 100%)}
.cover::after{content:"";position:absolute;right:-14px;top:10px;width:14px;height:calc(100% - 6px);background:linear-gradient(90deg,#e9e9e9,#bdbdbd);transform:skewY(8deg);transform-origin:left top}

/* about book */
.section-head{font-size:37px;line-height:41px}
.quote{left:604px;top:1085px;width:425px;text-align:right;color:var(--teal-deep);font-size:17.3px;line-height:26.6px;font-weight:500}
.quote-bar{left:1040px;top:1067px;width:5px;height:176px;background:var(--yellow)}

/* inside */
.red-band{left:0;top:1573px;width:1110px;height:486px;background:var(--red)}
.chapter-card{left:89px;top:1343px;width:492px;height:639px;background:var(--white);border-radius:34px;box-shadow:0 0 12px rgba(0,0,0,.18);padding:44px 26px 0 26px}
.chapter-card h3{font-size:34px;font-weight:600;color:var(--ink);margin-bottom:26px}
.chapter-card p{font-size:14px;line-height:30.3px;color:var(--ink);margin-bottom:30px}
.stat-num{font-size:45px;font-weight:900;color:var(--white);text-align:center;line-height:50px}
.stat-label{font-size:18px;color:var(--white);text-align:center;font-weight:400}
.inside-text{left:652px;top:1708px;width:390px;font-size:13.8px;line-height:26.8px;color:var(--white)}

/* author */
.author-photo{left:89px;top:2162px;width:438px;height:438px;border-radius:50%;background:radial-gradient(circle at 55% 40%,#d9c3ae 0%,#9e8a7a 35%,#5a5656 70%,#3a3d44 100%)}
.author-text{left:583px;width:500px;font-size:13.8px;line-height:26.8px;color:var(--ink)}
.author-quote{left:583px;top:2478px;width:500px;font-size:15.3px;line-height:26.8px;font-weight:700;color:var(--ink)}
.signature{left:583px;top:2578px;font-family:"Courgette",cursive;font-size:36px;color:var(--teal)}

/* upcoming */
.upcoming-title{left:0;width:1200px;top:2766px;text-align:center;font-size:40px}
.upcoming-book{position:absolute;top:2857px;width:161px;height:254px;box-shadow:-14px 6px 14px rgba(0,0,0,.3)}
.book-label{position:absolute;top:3121px;width:200px;text-align:center;font-size:18.5px;font-weight:800;color:var(--ink)}

/* promo */
.promo{left:89px;top:3282px;width:1021px;height:406px;background:var(--yellow)}
.promo-kicker{left:89px;top:3365px;width:562px;text-align:center;color:var(--white);font-size:20px;font-weight:700}
.promo-title{left:89px;top:3396px;width:562px;text-align:center;color:var(--white);font-size:35px;font-weight:800;letter-spacing:.5px}
.promo-text{left:150px;top:3444px;width:440px;text-align:center;color:var(--white);font-size:13.8px;line-height:24.5px}
.btn-outline{background:transparent;border:2px solid var(--white)}

/* footer */
.footer{left:0;top:3860px;width:1200px;height:367px;background:var(--navy)}
.footer-logo{left:0;width:1200px;top:3928px;text-align:center;font-size:76px;font-weight:900;color:var(--white);letter-spacing:2px}
.footer-nav a{color:var(--white);font-size:14.5px;font-weight:500}
.social{position:absolute;top:4097px;width:29px;height:29px;border:1.6px solid var(--white);border-radius:50%}
.footer-rule{left:89px;top:4186px;width:1021px;height:1px;background:rgba(255,255,255,.35)}
.footer-small{top:4201px;font-size:13.5px;color:var(--white)}
</style>
</head>
<body>

<!-- header & hero -->
<svg class="hero-shape" width="1200" height="720" viewBox="0 0 1200 720" aria-hidden="true">
  <defs>
    <linearGradient id="heroFade" x1="0.15" y1="0" x2="0.85" y2="0.9">
      <stop offset="0" stop-color="#ffffff"/>
      <stop offset="0.45" stop-color="#a7e4ec"/>
      <stop offset="1" stop-color="#19b4c6"/>
    </linearGradient>
  </defs>
  <path d="M250,0 L1200,0 L1200,445 C1140,525 1075,585 995,618 L660,420 Z" fill="url(#heroFade)"/>
</svg>

<div class="abs logo">ARP</div>
<nav class="nav" style="left:0;top:0">
  <a style="left:658px;top:41px">Home</a>
  <a style="left:732px;top:41px">Author</a>
  <a style="left:813px;top:41px">Inside</a>
  <a style="left:888px;top:41px">Upcoming</a>
</nav>
<a class="btn" style="left:988px;top:34px;width:122px;height:35px;font-size:14px">Shop Now</a>

<h1 class="abs display hero-title">Welcome To<br>Amber Ridge<br>Publishing</h1>
<p class="abs hero-text">It is a long established fact that a reader will be distracted by the readable content of a page when looking at its layout.</p>
<a class="btn" style="left:89px;top:568px;width:133px;height:36px">Shop Now</a>

<div class="cover cover-main" style="left:655px;top:104px;width:375px;height:612px;transform:rotate(1.5deg)" role="img" aria-label="Book cover of Silent Ledger by M.R. Theodor: dark blue night scene with a lightning strike and yellow title lettering"></div>

<!-- about the book -->
<svg class="abs" style="left:146px;top:796px" width="50" height="56" viewBox="0 0 50 56" fill="none" stroke="var(--teal)" stroke-width="2" aria-hidden="true">
  <rect x="4" y="4" width="42" height="48" rx="2"/>
  <line x1="10" y1="4" x2="10" y2="52"/>
  <rect x="18" y="14" width="20" height="8"/>
  <line x1="18" y1="32" x2="38" y2="32"/><line x1="18" y1="38" x2="38" y2="38"/>
</svg>
<h2 class="abs display section-head" style="left:217px;top:793px">ABOUT THE<br>BOOK</h2>
<p class="abs body-copy" style="left:148px;top:912px;width:420px">Lorem ipsum dolor sit amet, consectetur adipiscing elit, sed do eiusmod tempor incididunt ut labore et dolore magna aliqua. Ut enim ad minim veniam, quis nostrud exercitation ullamco laboris nisi ut aliquip ex ea commodo consequat. Duis aute irure dolor in reprehenderit in voluptate velit esse cillum dolore eu fugiat nulla pariatur.</p>
<p class="abs body-copy" style="left:148px;top:1099px;width:420px">Excepteur sint occaecat cupidatat non proident, sunt in culpa qui officia deserunt mollit anim id est laborum. Sed ut perspiciatis unde omnis iste natus error sit voluptatem accusantium doloremque laudantium, totam rem aperiam, eaque ipsa quae ab illo inventore.</p>
<p class="abs body-copy" style="left:604px;top:764px;width:420px">Lorem ipsum dolor sit amet, consectetur adipiscing elit, sed do eiusmod tempor incididunt ut labore et dolore magna aliqua. Ut enim ad minim veniam, quis nostrud exercitation ullamco laboris nisi ut aliquip ex ea commodo consequat. Duis aute irure dolor in reprehenderit in voluptate velit esse cillum dolore eu fugiat nulla pariatur. Excepteur sint occaecat cupidatat non proident, sunt in culpa qui officia deserunt mollit anim id est laborum. Sed ut perspiciatis unde omnis iste natus error sit voluptatem accusantium doloremque laudantium, totam rem aperiam, eaque ipsa quae ab illo inventore.</p>
<p class="abs quote">Sed ut perspiciatis unde omnis iste natus error sit voluptatem accusantium doloremque laudantium, totam rem aperiam, eaque ipsa quae ab illo inventore veritatis et quasi architecto beatae vitae dicta sunt explicabo.</p>
<div class="abs quote-bar"></div>
<a class="btn" style="left:895px;top:1243px;width:133px;height:36px">Know More</a>

<!-- what's inside -->
<div class="abs red-band"></div>
<article class="abs chapter-card">
  <h3>Chapter 1</h3>
  <p>Sed ut perspiciatis unde omnis iste natus error sit voluptatem accusantium doloremque laudantium, totam rem.</p>
  <p>Aperiam, eaque ipsa quae ab illo inventore veritatis et quasi architecto beatae vitae dicta sunt explicabo. Nemo enim ipsam voluptatem quia voluptas sit aspernatur aut odit aut fugit, sed quia consequuntur magni dolores eos qui ratione voluptatem sequi nesciunt. Neque porro quisquam est, qui dolorem ipsum quia dolor sit amet, consectetur, adipisci velit, sed quia non numquam eius modi tempora incidunt ut labore et dolore magnam aliquam quaerat voluptatem.</p>
  <p>&nbsp;Ut enim ad minima veniam, quis nostrum exercitationem ullam corporis suscipit laboriosam, nisi ut aliquid ex ea commodi consequatur Quis autem vel eum iure reprehenderit qui in ea voluptate velit.</p>
</article>

<svg class="abs" style="left:650px;top:1366px" width="72" height="60" viewBox="0 0 72 60" fill="none" stroke="var(--teal)" stroke-width="2" aria-hidden="true">
  <path d="M36 12 C28 6 16 5 6 7 V52 C16 50 28 51 36 56 C44 51 56 50 66 52 V7 C56 5 44 6 36 12 Z"/>
  <line x1="36" y1="12" x2="36" y2="56"/>
  <path d="M2 12 V58 H70 V12"/>
  <line x1="12" y1="18" x2="30" y2="20"/><line x1="12" y1="26" x2="30" y2="28"/><line x1="12" y1="34" x2="30" y2="36"/>
  <line x1="42" y1="20" x2="60" y2="18"/><line x1="42" y1="28" x2="60" y2="26"/><line x1="42" y1="36" x2="60" y2="34"/>
</svg>
<h2 class="abs display section-head" style="left:739px;top:1377px">WHAT’S INSIDE</h2>
<p class="abs" style="left:739px;top:1424px;width:378px;font-size:13.8px;line-height:26.8px;color:var(--ink)">Lorem ipsum dolor sit amet, consectetur adipiscing elit, sed do eiusmod tempor incididunt ut labore et dolore magna aliqua. Ut enim ad minim veniam, quis nostrud exercitation ullamco laboris</p>

<div class="abs" style="left:652px;top:1604px;width:75px">
  <div class="stat-num">22</div><div class="stat-label">Chapters</div>
</div>
<div class="abs" style="left:793px;top:1604px;width:90px">
  <div class="stat-num">250</div><div class="stat-label">Pages</div>
</div>
<p class="abs inside-text">At vero eos et accusamus et iusto odio dignissimos ducimus qui blanditiis praesentium voluptatum deleniti atque corrupti quos dolores et quas molestias excepturi sint occaecati cupiditate non provident, similique sunt in culpa qui officia deserunt mollitia animi, id est laborum et dolorum fuga.</p>
<a class="btn" style="left:652px;top:1888px;width:133px;height:36px">Buy Now</a>

<!-- about the author -->
<div class="abs author-photo" role="img" aria-label="Portrait photo of author M.R. Theodor smiling and holding a notebook"></div>
<svg class="abs" style="left:582px;top:2140px" width="54" height="56" viewBox="0 0 54 56" fill="none" stroke="var(--teal)" stroke-width="2" aria-hidden="true">
  <path d="M40 4 L50 14 L20 44 L6 48 L10 34 Z"/>
  <line x1="34" y1="10" x2="44" y2="20"/>
  <line x1="10" y1="34" x2="20" y2="44"/>
  <path d="M2 54 C14 50 26 52 40 50"/>
</svg>
<h2 class="abs display section-head" style="left:657px;top:2133px">ABOUT THE<br>AUTHOR</h2>
<p class="abs author-text" style="top:2253px">But I must explain to you how all this mistaken idea of denouncing pleasure and praising pain was born and I will give you a complete account of the system, and expound the actual teachings of the great explorer of the truth, the master-builder of human happiness. No one rejects, dislikes, or avoids pleasure itself, because it is pleasure.</p>
<p class="abs author-text" style="top:2414px">But because those who do not know how to pursue pleasure rationally encounter consequences that are extremely painful.</p>
<p class="abs author-quote">“Lorem ipsum dolor sit amet, consectetur adipiscing elit, sed do eiusmod tempor incididunt ut labore et dolore magna aliqua. Ut enim ad minim veniam, quis nostrud”</p>
<div class="abs signature">M.R. Theodor</div>

<!-- upcoming books -->
<svg class="abs" style="left:576px;top:2700px" width="50" height="58" viewBox="0 0 50 58" fill="none" stroke="var(--teal)" stroke-width="2" aria-hidden="true">
  <rect x="8" y="2" width="38" height="54" rx="2"/>
  <rect x="20" y="12" width="18" height="14"/>
  <path d="M3 10 H12 M3 18 H12 M3 26 H12 M3 34 H12 M3 42 H12 M3 50 H12"/>
</svg>
<h2 class="abs display upcoming-title">UPCOMING BOOKS</h2>

<div class="upcoming-book" style="left:87px;background:linear-gradient(180deg,#9fb4e8 0%,#3a4fa0 40%,#0f1740 100%)" role="img" aria-label="Book cover: figure in a blue moonlit forest"></div>
<div class="upcoming-book" style="left:380px;background:linear-gradient(180deg,#4a8a92 0%,#1e5a66 50%,#2a2228 85%,#c0571c 100%)" role="img" aria-label="Book cover: spooky teal forest with bats and pumpkins"></div>
<div class="upcoming-book" style="left:670px;background:linear-gradient(180deg,#c8d6e4 0%,#6f88a3 50%,#2f3f55 100%)" role="img" aria-label="Book cover: misty blue woodland"></div>
<div class="upcoming-book" style="left:949px;background:linear-gradient(180deg,#a6b8b8 0%,#45605e 45%,#0b0f0f 100%)" role="img" aria-label="Book cover: dark pine tree under lightning"></div>

<div class="book-label" style="left:70px">Lorem Ipsum</div>
<div class="book-label" style="left:362px">Lorem Ipsum</div>
<div class="book-label" style="left:654px">Lorem Ipsum</div>
<div class="book-label" style="left:933px">Lorem Ipsum</div>
<a class="btn" style="left:534px;top:3180px;width:132px;height:36px">Browse All</a>

<!-- promo banner -->
<div class="abs promo"></div>
<div class="abs promo-kicker">A Murder Mystery</div>
<div class="abs promo-title">SILENT LEDGER</div>
<p class="abs promo-text">Sed ut perspiciatis unde omnis iste natus error sit voluptatem accusantium doloremque laudantium, totam rem aperiam, eaque ipsa quae ab illo inventore veritatis et quasi architecto beatae vitae dicta sunt explicabo.</p>
<a class="btn btn-outline" style="left:292px;top:3561px;width:133px;height:36px">Buy Now</a>
<div class="cover cover-main" style="left:700px;top:3316px;width:302px;height:505px;transform:rotate(1.5deg)" role="img" aria-label="Book cover of Silent Ledger by M.R. Theodor: dark blue night scene with a lightning strike and yellow title lettering"></div>

<!-- footer -->
<footer>
  <div class="abs footer"></div>
  <div class="abs footer-logo">ARP</div>
  <nav class="nav footer-nav" style="left:0;top:0">
    <a style="left:448px;top:4044px">Home</a>
    <a style="left:522px;top:4044px">Author</a>
    <a style="left:603px;top:4044px">Inside</a>
    <a style="left:677px;top:4044px">Upcoming</a>
  </nav>
  <span class="social" style="left:516px" aria-label="Social link"></span>
  <span class="social" style="left:562px" aria-label="Social link"></span>
  <span class="social" style="left:608px" aria-label="Social link"></span>
  <span class="social" style="left:654px" aria-label="Social link"></span>
  <div class="abs footer-rule"></div>
  <div class="abs footer-small" style="left:89px">© 2019 All rights reserved.</div>
  <div class="abs footer-small" style="left:867px">Privacy Policy</div>
  <div class="abs footer-small" style="left:977px">Terms &amp; Conditions</div>
</footer>

</body>
</html>
```